RK Bastone Construction Inc.

Design a new business card for our construction company
To be removed from current card:
Delete 25 years
Delete Tenant fit up Renovations section

```html
<!DOCTYPE html>
<html lang="en">
<head>
<meta charset="utf-8">
<title>RK Bastone Construction Inc. – Business Card</title>
<link rel="stylesheet" href="https://fonts.googleapis.com/css2?family=Montserrat:wght@400;700;800&display=swap">
<style>
  :root {
    --purple: #573174;
    --teal: #20766c;
    --white: #ffffff;
    --ink: #3a3a3a;
    --backdrop: #9c9c9c;
  }
  * { margin: 0; padding: 0; box-sizing: border-box; }
  html, body {
    width: 1021px; height: 1200px; overflow: hidden;
    background: var(--backdrop);
    font-family: "Montserrat", sans-serif;
  }
  .card {
    position: absolute;
    left: 134px;
    width: 753px; height: 429px;
    border-radius: 26px;
    overflow: hidden;
  }
  .card--front { top: 119px; background: var(--white); }
  .card--back  { top: 651px; background: var(--purple); }

  .wave { position: absolute; inset: 0; width: 100%; height: 100%; }

  .company-name {
    position: absolute; left: 35px; top: 64px;
    font-weight: 700; font-size: 21px; letter-spacing: 0.3px;
    color: var(--purple);
  }
  .holder {
    position: absolute; right: 29px; top: 55px;
    text-align: right;
  }
  .holder__name {
    font-weight: 800; font-size: 27px; letter-spacing: 1px;
    color: var(--purple); line-height: 1.1;
  }
  .holder__name .surname { color: var(--teal); }
  .holder__title {
    font-weight: 400; font-size: 18px; color: var(--ink);
    line-height: 1.2;
  }

  .address {
    position: absolute; right: 29px; top: 252px;
    text-align: right; color: var(--white);
    font-style: normal;
    font-size: 16.5px; line-height: 21px; letter-spacing: 0.4px;
  }
  .contacts {
    position: absolute; right: 27px; top: 305px;
    list-style: none; color: var(--white);
    font-size: 16.5px; letter-spacing: 0.4px;
  }
  .contacts li {
    display: flex; justify-content: flex-end; align-items: center;
    gap: 9px; height: 24.5px;
  }
  .contacts svg { width: 13px; height: 13px; fill: var(--teal); flex: none; }

  .back-name {
    position: absolute; left: 0; right: 0; top: 174px;
    text-align: center; color: var(--white);
    font-weight: 700; font-size: 36px; letter-spacing: 0.5px;
  }
  .services {
    position: absolute; left: 0; right: 0; top: 364px;
    text-align: center; color: var(--white);
    font-size: 19px; letter-spacing: 2.2px; word-spacing: 6px;
  }
</style>
</head>
<body>

<section class="card card--front">
  <svg class="wave" viewBox="0 0 1300 741" preserveAspectRatio="none" aria-hidden="true">
    <path fill="var(--teal)" d="M0,449 C150,600 350,575 560,505 C760,405 900,300 1130,311 C1200,315 1260,340 1300,366 L1300,741 L0,741 Z"/>
    <path fill="var(--purple)" d="M0,512 C150,640 350,610 560,540 C760,440 900,340 1110,345 C1190,348 1250,378 1300,405 L1300,741 L0,741 Z"/>
    <path fill="none" stroke="var(--white)" stroke-width="8" d="M0,512 C150,640 350,610 560,540 C760,440 900,340 1110,345 C1190,348 1250,378 1300,405"/>
  </svg>

  <div class="company-name">RK Bastone Construction Inc.</div>

  <div class="holder">
    <div class="holder__name">MARC <span class="surname">BASTONE</span></div>
    <div class="holder__title">President</div>
  </div>

  <address class="address">
    1280 Ridgeline Ave., Suite 100<br>
    Ottawa, ON K2P 4B7
  </address>

  <ul class="contacts">
    <li>613-555-0142
      <svg viewBox="0 0 24 24"><path d="M6.6 10.8a15.1 15.1 0 0 0 6.6 6.6l2.2-2.2a1 1 0 0 1 1-.25 11.4 11.4 0 0 0 3.6.57 1 1 0 0 1 1 1V20a1 1 0 0 1-1 1A17 17 0 0 1 3 4a1 1 0 0 1 1-1h3.5a1 1 0 0 1 1 1c0 1.250.2 2.450.57 3.570a1 1 0 0 1-.25 1z"/></svg>
    </li>
    <li>613-555-0187 ext. 221
      <svg viewBox="0 0 24 24"><path d="M7 1h10a2 2 0 0 1 2 2v18a2 2 0 0 1-2 2H7a2 2 0 0 1-2-2V3a2 2 0 0 1 2-2zm0 3v14h10V4zm5 15.5a1 1 0 1 0 0 2 1 1 0 0 0 0-2z"/></svg>
    </li>
    <li>marc@rkbastoneconst.ca
      <svg viewBox="0 0 24 24"><path d="M2 5h20v2l-10 6L2 7zm0 4l10 6 10-6v10H2z"/></svg>
    </li>
    <li>www.rkbastoneconstruction.ca
      <svg viewBox="0 0 24 24"><path d="M12 2a10 10 0 1 0 0 20 10 10 0 0 0 0-20zm-1 2.1V8H7.6A8 8 0 0 1 11 4.1zm2 0A8 8 0 0 1 16.4 8H13zM6.8 10H11v4H6.8a8 8 0 0 1 0-4zm6.2 0h4.2a8 8 0 0 1 0 4H13zm-5.4 6H11v3.9A8 8 0 0 1 7.6 16zm5.4 0h3.4a8 8 0 0 1-3.4 3.9z"/></svg>
    </li>
  </ul>
</section>

<section class="card card--back">
  <div class="back-name">RK Bastone Construction Inc.</div>
  <div class="services">Office &nbsp;|&nbsp; Retail &nbsp;|&nbsp; Institutional</div>
</section>

</body>
</html>
```